https://copperwillowbrambleyard.org/

We would like the website to represent 19th century African American civil war soldier's letters. We would like the site colors to be nice and clean . Along with the layout, including a great landing page , blogs and introduction.

```html
<!DOCTYPE html>
<html lang="en">
<head>
<meta charset="utf-8">
<title>Copper Willow Brambleyard</title>
<link href="https://fonts.googleapis.com/css2?family=Rye&family=Zilla+Slab:wght@400;500;700&family=Open+Sans:wght@400&display=swap" rel="stylesheet">
<style>
:root{
  --bg-dark:#3a2e24;
  --bg-mid:#6b5a48;
  --paper:#e2d3b9;
  --ink:#3b3845;
  --accent:#7a4a1c;
  --text:#2f2a26;
  --muted:#6e655c;
  --white:#ffffff;
  --hero-1:#a8783e;
  --hero-2:#c89c5e;
  --hero-3:#6e4a22;
  --btn-light:#bfab92;
  --rule:#8a7c6a;
}
*{margin:0;padding:0;box-sizing:border-box}
html,body{width:820px;height:1200px;overflow:hidden}
body{
  position:relative;
  background:radial-gradient(ellipse at 50% 40%,var(--bg-mid),var(--bg-dark) 85%);
  font-family:"Zilla Slab",serif;
  color:var(--text);
}
.backdrop{position:absolute;inset:0}
.page{
  position:absolute;left:98px;top:55px;width:624px;height:1054px;
  background:var(--paper);
  box-shadow:0 0 20px rgba(0,0,0,.5);
}
.hero{
  position:absolute;left:0;top:0;width:624px;height:370px;
  background:radial-gradient(ellipse at 45% 45%,var(--hero-2),var(--hero-1) 55%,var(--hero-3));
}
.hero-edge{position:absolute;left:0;top:340px;width:624px;height:40px}
.site-title{
  position:absolute;top:12px;left:0;width:624px;text-align:center;
  font-family:"Rye",serif;font-size:28px;font-weight:400;color:var(--white);letter-spacing:.5px;
  text-shadow:0 2px 3px rgba(0,0,0,.5);
}
.nav{position:absolute;left:204px;top:54px;width:216px;height:26px}
.nav svg{position:absolute;inset:0}
.nav ul{
  position:absolute;inset:0;list-style:none;display:flex;justify-content:center;align-items:center;gap:6px;
  font-size:10.5px;color:var(--white);
}
.nav li.sep{font-size:8px}
.tagline{
  position:absolute;top:152px;left:0;width:624px;text-align:center;
  font-weight:700;font-size:21px;line-height:26px;color:var(--white);
  text-shadow:0 2px 4px rgba(0,0,0,.55);
}
.hero-btn{
  position:absolute;left:266px;top:212px;width:93px;height:32px;
  background:var(--btn-light);color:var(--ink);font-size:12px;
  display:flex;align-items:center;justify-content:center;
  box-shadow:0 2px 4px rgba(0,0,0,.35);
}
.dots{position:absolute;top:316px;left:286px;display:flex;gap:14px}
.dots span{width:8px;height:8px;border-radius:50%;background:var(--white)}
.dots span.active{background:var(--ink)}
.divider{position:absolute;left:427px;top:370px;width:1px;height:661px;background:var(--ink)}
.divider::before,.divider::after{content:"";position:absolute;left:-3.5px;width:8px;height:8px;border-radius:50%;background:var(--ink)}
.divider::before{top:-4px}.divider::after{bottom:-4px}
.post{position:absolute;left:17px;width:393px;height:191px;background:var(--white)}
.post-image{position:absolute;left:5px;top:5px;width:142px;height:181px}
.post-body{position:absolute;left:158px;top:8px;width:225px}
.post-title{font-size:13px;line-height:17.5px;color:var(--accent);font-weight:400;height:36px}
.post-meta{
  margin-top:5px;border-top:1px solid #ccc;border-bottom:1px solid #ccc;
  padding:6px 3px;font-size:6.2px;color:var(--accent);white-space:nowrap;
}
.post-excerpt{
  margin-top:8px;padding-left:3px;font-family:"Open Sans",sans-serif;font-size:6.7px;line-height:13px;color:var(--muted);height:66px;overflow:hidden;
}
.read-more{
  display:inline-flex;margin:9px 0 0 3px;width:60px;height:21px;background:var(--ink);color:var(--white);
  font-size:7.5px;align-items:center;justify-content:center;
}
.older{
  position:absolute;left:17px;top:1008px;width:71px;height:27px;background:var(--ink);color:var(--white);
  font-size:10px;display:flex;align-items:center;justify-content:center;
}
.sidebar{position:absolute;left:445px;top:398px;width:168px}
.search{
  height:27px;background:var(--white);display:flex;align-items:center;justify-content:space-between;
  padding:0 10px;font-family:"Open Sans",sans-serif;font-size:7.5px;color:var(--muted);
}
.intro{margin-top:13px;font-size:10px;line-height:18.6px;color:var(--text);padding-bottom:10px;border-bottom:1px solid var(--rule)}
.side-heading{font-size:13px;font-weight:400;color:var(--accent);margin:15px 0 0 3px}
.social{display:flex;gap:6px;margin:10px 0 0 4px;padding-bottom:15px;border-bottom:1px solid var(--rule)}
.social span{
  width:32px;height:32px;border-radius:50%;background:var(--ink);color:var(--white);
  font-size:7px;display:flex;align-items:center;justify-content:center;
}
.contact-line{display:flex;align-items:center;gap:9px;margin:10px 0 0 4px;font-size:13px;color:var(--ink);white-space:nowrap}
.contact-line.email{font-size:12px}
.footer{
  position:absolute;top:1142px;left:0;width:820px;text-align:center;font-size:13px;color:var(--white);
}
</style>
</head>
<body>
<div class="backdrop" role="img" aria-label="Faded pages of handwritten nineteenth-century letters"></div>

<main class="page">
  <section class="hero" role="img" aria-label="Stack of old envelopes and letters tied with string"></section>
  <svg class="hero-edge" viewBox="0 0 624 40" preserveAspectRatio="none" aria-hidden="true">
    <path d="M0 10 L14 3 L26 12 L40 5 L55 13 L70 6 L88 14 L104 7 L120 15 L140 8 L160 14 L180 9 L200 16 L222 10 L246 17 L270 11 L295 18 L320 12 L345 19 L372 13 L400 19 L428 14 L456 20 L484 15 L512 21 L540 16 L566 22 L590 18 L610 24 L624 20 L624 40 L0 40 Z" fill="#e2d3b9"/>
    <path d="M0 10 L14 3 L26 12 L40 5 L55 13 L70 6 L88 14 L104 7 L120 15 L140 8 L160 14 L180 9 L200 16 L222 10 L246 17 L270 11 L295 18 L320 12 L345 19 L372 13 L400 19 L428 14 L456 20 L484 15 L512 21 L540 16 L566 22 L590 18 L610 24 L624 20" fill="none" stroke="#c89668" stroke-width="2"/>
  </svg>

  <h1 class="site-title">COPPER WILLOW BRAMBLEYARD</h1>
  <nav class="nav">
    <svg viewBox="0 0 216 26" preserveAspectRatio="none" aria-hidden="true"><path d="M0 0 H216 L206 13 L216 26 H0 L10 13 Z" fill="#3b3845"/></svg>
    <ul><li>Home</li><li class="sep">•</li><li>About</li><li class="sep">•</li><li>Blog</li><li class="sep">•</li><li>Contact</li></ul>
  </nav>
  <p class="tagline">Exploring the lives and letters of men<br>who served in the USCT</p>
  <div class="hero-btn">READ MORE</div>
  <div class="dots"><span class="active"></span><span></span><span></span></div>

  <div class="divider"></div>

  <article class="post" style="top:398px">
    <div class="post-image" role="img" aria-label="Express company receipt and orange shipping labels on a desk" style="background:linear-gradient(135deg,#8a5a34,#d8c9bd 45%,#c8702c 75%,#6a4226)"></div>
    <div class="post-body">
      <h2 class="post-title">"I'm well and doing well as a soldier can expect..."</h2>
      <p class="post-meta">By quillkeeper7 &nbsp;| &nbsp;February 16, 2020 &nbsp;| &nbsp;No Comments &nbsp;| &nbsp;Sticky post</p>
      <p class="post-excerpt">Cole's ninth letter in this collection was written December 29th, 1864 while he and his regiment were in Beaufort, South Carolina. His letter opens with acknowledging the receipt of his mother's last letter. We also find that Cole has made good on his promise to send his family some money.</p>
      <span class="read-more">Read More</span>
    </div>
  </article>

  <article class="post" style="top:600px">
    <div class="post-image" role="img" aria-label="Old postcard and reading glasses beside a laptop on a desk" style="background:linear-gradient(135deg,#3a2418,#a8642c 45%,#d9c8a8 65%,#7a4420)"></div>
    <div class="post-body">
      <h2 class="post-title">Freedom by sword and pen...</h2>
      <p class="post-meta">By quillkeeper7 &nbsp;| &nbsp;February 16, 2020 &nbsp;| &nbsp;No Comments &nbsp;| &nbsp;Sticky post</p>
      <p class="post-excerpt">My Dear mother I Recied your kind leter and i was more then glad to hear that you was well and to hear that get the money saft i sent to you &nbsp; i am well at this time and i truley hope these few lines may find you the same &nbsp; i have not much news to tel you this time onley part of my Rigment is out on main land a Fiting the</p>
      <span class="read-more">Read More</span>
    </div>
  </article>

  <article class="post" style="top:802px">
    <div class="post-image" role="img" aria-label="Scanned handwritten letter page" style="background:linear-gradient(90deg,#cfcfcf,#ebebeb 40%,#dedede)"></div>
    <div class="post-body">
      <h2 class="post-title">Maecenas vel tortor accumsan quam varius imperdiet</h2>
      <p class="post-meta">By quillkeeper7 &nbsp;| &nbsp;February 16, 2020 &nbsp;| &nbsp;No Comments &nbsp;| &nbsp;Sticky post</p>
      <p class="post-excerpt">&nbsp;We also get a first-hand account of the food scarcity many soldiers faced at this time as Cole notes that he is near starvation. While this statement may be somewhat hyperbolic, it may not be too far off from the truth. Despite the fact that Cole has sent money to his mother, he is now requesting that she send him</p>
      <span class="read-more">Read More</span>
    </div>
  </article>

  <div class="older">Older Post</div>

  <aside class="sidebar">
    <div class="search"><span>Search</span>
      <svg width="9" height="9" viewBox="0 0 10 10" aria-hidden="true"><circle cx="4" cy="4" r="3" fill="none" stroke="#3b3845" stroke-width="1.5"/><line x1="6.2" y1="6.2" x2="9.3" y2="9.3" stroke="#3b3845" stroke-width="1.6"/></svg>
    </div>
    <p class="intro">Welcome to this blog dedicated to Thaddeus L. Brennick and devoted to sharing the letters, lives, and images of black men who served in the United States Colored Troops during the American Civil War. In honor of Dr. Amos Whitcombe, this blog seeks to “right a great wrong” and tell the stories of those men who bravely fought to free themselves, their brothers and sisters, and maintain the union of this country. Enjoy!</p>
    <h3 class="side-heading">Follow us on</h3>
    <div class="social"><span>News</span><span>Talk</span><span>Board</span><span>Photo</span></div>
    <h3 class="side-heading">Contact</h3>
    <p class="contact-line">
      <svg width="12" height="12" viewBox="0 0 24 24" aria-hidden="true"><path d="M6.6 10.8a15 15 0 0 0 6.6 6.6l2.2-2.2a1 1 0 0 1 1-.25 11.4 11.4 0 0 0 3.6.57 1 1 0 0 1 1 1V20a1 1 0 0 1-1 1A17 17 0 0 1 3 4a1 1 0 0 1 1-1h3.5a1 1 0 0 1 1 1c0 1.25.2 2.45.57 3.57a1 1 0 0 1-.25 1z" fill="#3b3845"/></svg>
      555 014 2290</p>
    <p class="contact-line email">
      <svg width="13" height="10" viewBox="0 0 26 20" aria-hidden="true"><rect width="26" height="20" rx="2" fill="#3b3845"/><path d="M1 2 L13 11 L25 2" fill="none" stroke="#e2d3b9" stroke-width="2"/></svg>
      info@cwbrambleyard.org</p>
  </aside>
</main>

<footer class="footer">Copyright &nbsp;© &nbsp;2020 &nbsp;Copper Willow Brambleyard. &nbsp;All rights reserved.</footer>
</body>
</html>
```